Start-up braucht modernes/hochwertiges Getränkeetikett
Zielgruppe
Wir sind ein modernes, nachhaltiges Start-up, welches eine neue Getränkekategorie auf den Markt bringt. Ein sogenanntes Elektrolyt-Getränk mit dem Namen KLORV5. Es ist abgefüllt in eine 500 ml Flasche und enthält Magnesium, Kalzium, Kalium, und Natrium. Diese Stoffe (Elektrolyte) dienen der körperlichen Hydrierung. Zu Dehydrierung kann es durch Hitze, Alkohol, Sport oder Krankheit kommen. Krankheit liegt bei uns allerdings nicht im Fokus. In unserer Zielgruppe befinden sich hauptsächlich Personen im Alter von 18 - 29 Jahren.
Die Geschmacksrichtung ist Zitrone-Limette.
Aufgabenstellung
Das Etikett soll:
- MODERN, SCHLICHT und HOCHWERTIG sein, so dass es im Supermarkt hervorsticht
- erkenntlich machen, dass die Stoffe Magnesium, Natrium, Kalzium und Kalium enthalten sind
- sich farblich deutlich von der Farbe des Inhalts (weiß) abheben. (Vorzugsweise mit einem hellen Blau, türkis)
- für unsere junge Zielgruppe ansprechend sein
- ebenfalls auf die Geschmacksrichtung (Zitrone-Limette) hinweisen, und zwar so, dass wenn man eine weitere Geschmacksrichtung auf den Markt bringen möchte, diese leicht angepasst werden kann.
- nicht nach einem Energydrink oder einem typischen Sportgetränk aussehen
- unter dem Namen den Slogan 'Elektrolyt-Getränk' stehen haben
-Das Etikett ist nicht dursichtig sondern besteht aus Papier
Der Name sowie das Logo können selbstverständlich farblich verändert werden. Bei dem Logo können auch größere Änderungen vollzogen werden.
Bitte beachten Sie die unten zu stehenden Regler um sich einen guten Überblick über unsere Vorstellungen zu verschaffen. Die Platzierung des EAN-Code ist für ihr Design irrelevat .
Bei Unklarheiten gerne nachfragen!

```html
<!DOCTYPE html>
<html lang="de">
<head>
<meta charset="utf-8">
<title>KLORV5 Elektrolyt-Getränk – Etikett</title>
<link href="https://fonts.googleapis.com/css2?family=Montserrat:wght@500;700;800&family=Inter:wght@400;600;700&display=swap" rel="stylesheet">
<style>
  :root {
    --stage: #a8c5eb;
    --label-light: #f4f7fa;
    --label-water: #dde8f1;
    --brand: #c4d2e2;
    --tagline: #8eaed3;
    --ion: #111111;
    --panel: #ffffff;
    --fine: #2a2f36;
  }
  * { margin: 0; padding: 0; box-sizing: border-box; }
  html, body {
    width: 1200px; height: 3009px; overflow: hidden;
    background: var(--stage);
  }
  .label {
    position: absolute; left: 0; top: 904px;
    width: 1200px; height: 1168px; overflow: hidden;
    font-family: "Inter", sans-serif;
  }
  .label__texture {
    position: absolute; inset: 0;
    background:
      radial-gradient(ellipse at 30% 20%, var(--label-light) 0%, transparent 60%),
      radial-gradient(ellipse at 75% 80%, var(--label-light) 0%, transparent 55%),
      linear-gradient(160deg, var(--label-water), var(--label-light) 45%, var(--label-water));
  }
  .upward {
    position: absolute;
    writing-mode: vertical-rl;
    transform: rotate(180deg);
    white-space: nowrap;
  }
  .downward {
    position: absolute;
    writing-mode: vertical-rl;
    white-space: nowrap;
  }
  .info-strip {
    left: 20px; top: 60px; width: 100px; height: 480px;
    font-size: 20px; line-height: 32px; color: var(--fine);
  }
  .volume {
    left: 40px; top: 600px; width: 50px; height: 150px;
    font-size: 32px; font-weight: 700; color: var(--fine);
  }
  .brand-name {
    left: 130px; top: 60px; width: 180px; height: 760px;
    font-family: "Montserrat", sans-serif; font-weight: 800;
    font-size: 140px; line-height: 180px; letter-spacing: 2px;
    color: var(--brand);
  }
  .tagline {
    left: 320px; top: 110px; width: 80px; height: 650px;
    font-family: "Montserrat", sans-serif; font-weight: 700;
    font-size: 54px; line-height: 80px; color: var(--tagline);
  }
  .ion-panels { position: absolute; left: 440px; top: 0; width: 420px; height: 1168px; }
  .ion {
    position: absolute; left: 510px; width: 180px;
    font-family: "Montserrat", sans-serif; font-weight: 800;
    font-size: 100px; line-height: 180px; color: var(--ion);
    text-align: center;
  }
  .ion sup { font-size: 52px; vertical-align: 0.9em; line-height: 0; }
  .ion--k  { top: 20px;  height: 250px; }
  .ion--ca { top: 300px; height: 260px; }
  .ion--na { top: 590px; height: 260px; }
  .ion--mg { top: 880px; height: 270px; }
  .nutrition {
    right: 30px; top: 40px; width: 290px; height: 560px;
    font-size: 26px; line-height: 44px; color: var(--fine);
  }
  .nutrition__title { font-weight: 700; font-size: 28px; }
  .ingredients {
    right: 40px; top: 780px; width: 280px; height: 360px;
    font-size: 24px; line-height: 42px; color: var(--fine);
  }
</style>
</head>
<body>
  <section class="label">
    <div class="label__texture" role="img" aria-label="Heller Wasserflächen-Hintergrund in zartem Blau"></div>

    <div class="upward info-strip">
      Zitrone-Limette Geschmack<br>
      Ohne Zuckerzusatz, vegan<br>
      Kühl und trocken lagern
    </div>
    <div class="upward volume">500 ml</div>

    <div class="upward brand-name">KLORV5</div>
    <div class="upward tagline">Elektrolyt-Getränk</div>

    <svg class="ion-panels" viewBox="0 0 420 1168" aria-hidden="true">
      <polygon fill="#ffffff" points="0,0 340,0 400,135 340,270 0,270 40,135"/>
      <polygon fill="#ffffff" points="0,290 340,290 400,425 340,560 0,560 40,425"/>
      <polygon fill="#ffffff" points="0,580 340,580 400,715 340,850 0,850 40,715"/>
      <polygon fill="#ffffff" points="0,870 340,870 400,1019 340,1168 0,1168 40,1019"/>
    </svg>

    <div class="upward ion ion--k">K<sup>+</sup></div>
    <div class="upward ion ion--ca">Ca<sup>2+</sup></div>
    <div class="upward ion ion--na">Na<sup>2+</sup></div>
    <div class="upward ion ion--mg">Mg<sup>2+</sup></div>

    <div class="downward nutrition">
      <span class="nutrition__title">Elektrolyte pro Flasche</span><br>
      Magnesium 60 mg<br>
      Natrium 230 mg<br>
      Kalzium 80 mg<br>
      Kalium 150 mg
    </div>
    <div class="downward ingredients">
      Zutaten: Wasser,<br>
      Zitronen- und Limettensaft,<br>
      Mineralsalze, Aroma.<br>
      Gekühlt genießen.
    </div>
  </section>
</body>
</html>
```